Bold, Modern, Clean "Quarvenstretch.com" website

Why we stand out?
We are a male and female mobile massage team. Our names are Todd and Lise. 
Quarven Tide is a Seattle based mobile massage service. Our massage is offered to the community with a goal of facilitating balance within each individual. We specialize in integrated Pain management, and sports/medical massage therapy. Every client's first assessment is attended by our male and female massage therapist team. Depending on the goals identified for an individual determines which therapist will be assigned to provide treatment, if not both.

Our passion...
Here at Quarven Tide, we have a great passion for Postural Resoration and how it is integrated into an individual's Massage treatment. We pride ourselves in being natural facilitators of healing, which takes the ego of the therapist out of the client's healing process. We strive to deliver the best massage possible by including modalities such as Neuromuscular, Myofascial release, spontaneous muscle release, postural restoration, orthopedic, and medical massage.

Our education...

We are both Graduates of Halvenor, school of massage therapy. We have continuing education in medical massage, myofacial release, trigger point therapy, postural restoration, anatomy, and spontaneous muscle release. Lise is also a Certified Yoga Instructor, which amplifies her experience with flexibility and strength as it pertains to each individual. Todd's passion is Massage, stretching, and strength training to encourage postural restoration and realignment.

Our rates-

Our rates are $75/ 60 minutes, $95/ 90 minutes, and $120/ 120 minutes.

Education-
Both Lise and I worked as behavioral health professionals that specialized in life skills mentoring for youth who had experienced different types of trauma. This led us both to want to help others in a different environment, where individuals can be empowered to take responsibility over their own healing. To us, massage is a type of manipulation physical therapy, that encourages healing on many levels.

Advice to any massage client-
The most important thing to 'us', as Licenced providers is to get you on to our table to show you our skills. But a good therapist never forgets that it's not about what we do for you, but what we can facilitate for you. Your health and healing has nothing to do with us. It is yours, not ours. Identify what your goals are with any Therapist, and know what the end looks like. Progress should be tangible, such as range of motion, and decreased pain.

5/5 stars Massage Therapy
Verified Review

Lise and Todd at Quarven Tide are awesome! I recently had open heart surgery, and Lise worked on me to increase my range of motion while helping with the pinched nerve from my arm being in the same position for so long during my surgery. My wife drives a lot for work, and Todd has helped decrease her neck and lower back pain immensely. They are seriously the best therapists I have ever worked with. I would recommend them to anyone who needs anything from stress relief to a medical massage treatment. They are professional, up beat, easy going, and always on time. And, I love that they meet us where ever we like! We did a staycation recently, where they came to our hotel to give us relaxation massages. Although usually they come to our home, where we focus on pain related issues. We will continue to work with them for a long, long time.

Bressa K. on December 17, 2015

Target Market(s)

Mobile massage therapy clients

Industry/Entity Type

Massage Therapy

Font styles to use
Serif
Sans Serif

Requirements
Must have
• Please add or remove any information that would help the presentation of our website. Our logo is posted below, please include into the website.
• Please include a contact field that includes, quarvenstretch@mailbrook.net,
• (206) 555-0194
• We have also included our own stock photos, as well as a photo of Todd and Lise. Please include a cropped photo of both massage therapists.

```html
<!DOCTYPE html>
<html lang="en">
<head>
<meta charset="utf-8">
<title>Quarven Tide – Mobile Massage</title>
<link rel="stylesheet" href="https://fonts.googleapis.com/css2?family=Raleway:wght@400;500;600&family=Open+Sans:wght@400;600&family=Great+Vibes&display=swap">
<style>
:root{
  --blue:#1a7ad8;
  --blue-light:#4aa3ea;
  --dark:#2b2b2b;
  --darker:#1f1f1f;
  --ink:#333;
  --muted:#777;
  --white:#fff;
  --line:#d8d8d8;
}
*{box-sizing:border-box;margin:0;padding:0}
html,body{width:1200px;height:4082px;overflow:hidden}
body{position:relative;background:var(--white);font-family:"Open Sans",Arial,sans-serif;color:var(--ink)}
.abs{position:absolute}
.center{left:0;width:1200px;text-align:center}
.heading{font-family:"Raleway",Arial,sans-serif;font-weight:500;font-size:42px;color:var(--blue);letter-spacing:1px}
.heading-rule{position:absolute;left:500px;width:200px;height:3px;background:var(--line)}
.script{font-family:"Great Vibes",cursive;font-size:24px;color:var(--ink)}
.on-dark{color:var(--white)}

/* top bar */
.topbar{top:0;left:0;width:1200px;height:44px;background:var(--dark);color:var(--white);font-size:14px}
.topbar .call{left:80px;top:13px;letter-spacing:.5px}
.topbar svg{position:absolute;left:48px;top:12px}
.social{display:flex;gap:14px}
.social span{width:14px;height:14px;border-radius:50%;background:#bbb;display:block}
.topbar .social{position:absolute;right:80px;top:15px}

/* nav */
.nav{top:44px;left:0;width:1200px;height:81px;background:var(--white);font-family:"Raleway",sans-serif;font-weight:600;font-size:16px}
.nav a{position:absolute;top:31px;color:var(--ink);text-decoration:none}
.nav a.active{color:var(--blue)}
.city{position:absolute;left:938px;top:0;width:262px;height:81px;background:var(--blue)}
.city .select{position:absolute;left:20px;top:18px;width:162px;height:40px;background:var(--white);color:var(--ink);font-size:14px;padding:11px 14px}
.city .select svg{position:absolute;right:14px;top:16px}
.brand{left:520px;top:2px;width:160px;height:160px;border-radius:50%;background:var(--blue);border:6px solid var(--white);box-shadow:0 0 0 3px var(--blue);display:flex;align-items:center;justify-content:center;flex-direction:column;z-index:3;color:var(--white);font-family:"Raleway",sans-serif;font-weight:600;font-size:22px;text-align:center;line-height:1.15}

/* hero */
.hero{top:125px;left:0;width:1200px;height:533px;background:linear-gradient(120deg,#c9a27a 0%,#e8c9a7 40%,#b07d55 75%,#7a5338 100%)}
.dots{position:absolute;top:597px;left:548px;display:flex;gap:26px}
.dots span{width:14px;height:14px;border-radius:50%;border:2px solid var(--white);display:block}
.dots span.on{background:var(--white)}

/* welcome */
.welcome-photo{left:237px;top:835px;width:726px;height:182px;background:linear-gradient(90deg,#7a2a20,#c96a4b 45%,#e9c6a8)}
.intro{left:264px;top:1055px;width:672px;text-align:center;font-size:15px;line-height:26px}
.btn{position:absolute;height:52px;color:var(--white);font-size:14px;letter-spacing:1px;display:flex;align-items:center;padding-left:38px}
.btn .arrow{position:absolute;right:0;top:0;width:52px;height:52px;display:flex;align-items:center;justify-content:center}
.btn-blue{background:var(--blue)}
.btn-blue .arrow{background:var(--dark);top:10px;right:-8px}
.btn-dark{background:var(--dark)}
.btn-dark .arrow{background:var(--blue);top:10px;right:-8px}

/* call band */
.callband{top:1265px;left:0;width:1200px;height:307px;background:linear-gradient(90deg,#4a3a2c,#8a6a50 40%,#c9a583 70%,#6d4e3a)}
.callband .phone{top:1340px;font-family:"Raleway",sans-serif;font-size:60px;color:var(--white)}

/* passion */
.treat{position:absolute;width:130px;height:130px;border-radius:50%;background:#e6e6e6;border:4px solid #f3f3f3;box-shadow:0 0 0 1px #ddd}
.treat-label{left:120px;top:1763px;font-family:"Raleway",sans-serif;font-size:18px;color:var(--blue)}
.treat-text{left:96px;top:1795px;width:160px;font-size:14px;line-height:22px;text-align:right;color:var(--ink)}
.passion-photo{left:370px;top:1740px;width:514px;height:436px;background:radial-gradient(ellipse at 50% 50%,#e9dbd0 0%,#f6f1ec 55%,#ffffff 75%)}

/* testimonial */
.reviews{top:2252px;left:0;width:1200px;height:522px;background:linear-gradient(90deg,#2d2520,#4a3b30 50%,#2a221d)}
.avatar{left:556px;top:2453px;width:88px;height:88px;border-radius:50%;background:linear-gradient(#9a8878,#5e5048);border:4px solid var(--white)}
.quote{left:230px;top:2565px;width:740px;text-align:center;font-size:15px;line-height:27px;color:var(--white)}
.reviewer{top:2648px;font-family:"Raleway",sans-serif;font-size:18px;color:var(--blue-light)}
.date{top:2680px;font-size:15px;color:var(--white)}
.slide-arrow{position:absolute;top:2585px;width:32px;height:32px;border-radius:50%;border:2px solid #aaa}

/* team */
.member-photo{position:absolute;width:204px;height:310px}
.member-bar{position:absolute;height:49px;background:var(--dark);color:var(--white);font-family:"Raleway",sans-serif;font-size:20px;padding:12px 40px}
.member-bar .arrow{position:absolute;right:0;top:8px;width:46px;height:49px;background:var(--blue);display:flex;align-items:center;justify-content:center}
.member-list{position:absolute;width:280px;font-size:14px;line-height:22px;list-style:none}
.member-list li{margin-bottom:10px}
.price{position:absolute;width:58px;height:52px;background:var(--blue);color:var(--white);font-size:22px;display:flex;align-items:center;justify-content:center}

/* contact */
.contact{top:3340px;left:0;width:1200px;height:522px;background:linear-gradient(90deg,#2a2a2a,#4b4745 55%,#333)}
.field{position:absolute;height:49px;border:1px solid rgba(255,255,255,.55);background:rgba(255,255,255,.12);color:var(--white);font-size:14px;padding:14px 14px}
.submit{left:82px;top:3737px;width:1036px;height:52px;background:var(--blue);color:var(--white);font-size:18px;letter-spacing:1px;display:flex;align-items:center;justify-content:center}

/* info strip */
.info{top:3862px;left:0;width:1200px;height:150px;background:linear-gradient(135deg,#3d98e2,#5aaef0 50%,#3a92dc)}
.info-item{position:absolute;top:3888px;width:320px;text-align:center;color:var(--white);font-size:15px}
.info-item svg{display:block;margin:0 auto 20px}

/* footer */
.footer{top:4012px;left:0;width:1200px;height:70px;background:var(--darker);color:#ccc;font-size:14px}
.footer .copy{position:absolute;left:82px;top:26px}
.footer .copy b{color:var(--blue);font-weight:400}
.footer .social{position:absolute;right:82px;top:28px;gap:24px}
</style>
</head>
<body>

<header class="topbar abs">
  <svg width="20" height="20" viewBox="0 0 24 24"><path d="M6.6 10.8a15 15 0 0 0 6.6 6.6l2.2-2.2c.3-.3.7-.4 1-.2 1.1.4 2.3.6 3.6.6.6 0 1 .4 1 1V20c0 .6-.4 1-1 1A17 17 0 0 1 3 4c0-.6.4-1 1-1h3.5c.6 0 1 .4 1 1 0 1.3.2 2.5.6 3.6.1.3 0 .7-.2 1z" fill="#fff"/></svg>
  <div class="call abs">CALL US ON : (206) 555-0194</div>
  <div class="social" aria-label="Social links"><span></span><span></span><span></span></div>
</header>

<nav class="nav abs">
  <a class="active" style="left:82px">HOME</a>
  <a style="left:163px">ABOUT</a>
  <a style="left:258px">SERVICES</a>
  <a style="left:373px">PRICING</a>
  <a style="left:756px">BLOG</a>
  <a style="left:840px">CONTACT</a>
  <div class="city">
    <div class="select">SELECT CITY
      <svg width="12" height="8" viewBox="0 0 12 8"><path d="M0 0h12L6 8z" fill="var(--blue)"/></svg>
    </div>
  </div>
</nav>

<div class="brand abs">Quarven<br>Tide</div>

<section class="hero abs" role="img" aria-label="Photo of a woman relaxing during a massage with candles and flowers"></section>
<div class="dots"><span class="on"></span><span></span><span></span></div>

<section>
  <div class="heading-rule" style="top:712px"></div>
  <h1 class="heading abs center" style="top:724px">WELCOME</h1>
  <p class="script abs center" style="top:780px">One Of The Best Seattle based Mobile Massage Service.</p>
  <div class="welcome-photo abs" role="img" aria-label="Photo of a client receiving a back massage"></div>
  <p class="intro abs">We are a male and female mobile massage team. Our names are Todd and Lise. Quarven Tide is a Seattle based mobile massage service. Our massage is offered to the community with a goal of facilitating balance within each individual.</p>
  <div class="btn btn-blue" style="left:500px;top:1148px;width:192px">LEARN MORE
    <span class="arrow"><svg width="30" height="30" viewBox="0 0 30 30"><circle cx="15" cy="15" r="12" fill="none" stroke="#fff" stroke-width="2"/><path d="M13 10l5 5-5 5" fill="none" stroke="#fff" stroke-width="2"/></svg></span>
  </div>
</section>

<section class="callband abs" role="img" aria-label="Photo of a shoulder massage beside spa stones and candles"></section>
<div class="phone abs center" style="top:1340px;font-family:'Raleway',sans-serif;font-size:60px;color:#fff">(206) 555-0194</div>
<div class="btn btn-dark" style="left:500px;top:1433px;width:192px">CALL NOW
  <span class="arrow"><svg width="30" height="30" viewBox="0 0 30 30"><circle cx="15" cy="15" r="12" fill="none" stroke="#fff" stroke-width="2"/><path d="M13 10l5 5-5 5" fill="none" stroke="#fff" stroke-width="2"/></svg></span>
</div>

<section>
  <div class="heading-rule" style="top:1625px"></div>
  <h2 class="heading abs center" style="top:1638px">OUR PASSION</h2>
  <p class="script abs center" style="top:1700px">Select the Massage Therapy you want..</p>
  <div class="treat-label abs">Neuromuscular</div>
  <p class="treat-text abs">Lorem Ipsum is simply dummy text of the printing and typesetting.</p>
  <div class="treat" style="left:275px;top:1750px" role="img" aria-label="Neuromuscular therapy photo"></div>
  <div class="treat" style="left:185px;top:1893px" role="img" aria-label="Myofascial release photo"></div>
  <div class="treat" style="left:207px;top:2043px" role="img" aria-label="Spontaneous muscle release photo"></div>
  <div class="treat" style="left:800px;top:1750px" role="img" aria-label="Postural restoration photo"></div>
  <div class="treat" style="left:887px;top:1893px" role="img" aria-label="Orthopedic massage photo"></div>
  <div class="treat" style="left:873px;top:2043px" role="img" aria-label="Medical massage photo"></div>
  <div class="passion-photo abs" role="img" aria-label="Photo of a woman seated in white clothing"></div>
</section>

<section class="reviews abs" role="img" aria-label="Photo of running shoes on a wooden floor"></section>
<div class="heading-rule" style="top:2310px"></div>
<h2 class="heading abs center" style="top:2330px">5/5 STARS Massage Therapy</h2>
<p class="script abs center on-dark" style="top:2388px">What Clients say About us</p>
<div class="avatar abs" role="img" aria-label="Reviewer portrait"></div>
<p class="quote abs">Lise and Todd at Quarven Tide are awesome! I recently had open heart surgery, and Lise worked on me to increase my range of motion while helping with the pinched nerve from my arm being in the same position for so long during my surgery.</p>
<div class="reviewer abs center">Bressa K.</div>
<div class="date abs center">December 17, 2015</div>
<span class="slide-arrow" style="left:106px"></span>
<span class="slide-arrow" style="left:1058px"></span>

<section>
  <div class="heading-rule" style="top:2825px"></div>
  <h2 class="heading abs center" style="top:2840px">OUR TEAM</h2>
  <p class="script abs center" style="top:2894px">Know more About Us</p>

  <div class="member-photo" style="left:82px;top:2973px;background:linear-gradient(#8aa07a,#5c6a56)" role="img" aria-label="Cropped photo of Lise"></div>
  <div class="price" style="left:242px;top:3231px">$75</div>
  <div class="member-bar" style="left:307px;top:2973px;width:237px">Lise
    <span class="arrow"><svg width="28" height="28" viewBox="0 0 30 30"><circle cx="15" cy="15" r="12" fill="none" stroke="#fff" stroke-width="2"/><path d="M13 10l5 5-5 5" fill="none" stroke="#fff" stroke-width="2"/></svg></span>
  </div>
  <ul class="member-list" style="left:307px;top:3058px">
    <li>• Graduates - Halvenor, school of massage therapy.Continue with medical massage, my facial release, trigger point therapy, postural restoration, anatomy, and spontaneous muscle release.</li>
    <li>• Also a Certified Yoga Instructor.</li>
    <li>• $75/ 60 minutes.</li>
    <li>• $95/ 90 minutes.</li>
    <li>• $120/ 120 minutes.</li>
  </ul>

  <div class="member-photo" style="left:607px;top:2973px;background:linear-gradient(#b9c4c8,#6f7b80)" role="img" aria-label="Cropped photo of Todd"></div>
  <div class="price" style="left:770px;top:3231px">$75</div>
  <div class="member-bar" style="left:835px;top:2973px;width:240px">Todd
    <span class="arrow"><svg width="28" height="28" viewBox="0 0 30 30"><circle cx="15" cy="15" r="12" fill="none" stroke="#fff" stroke-width="2"/><path d="M13 10l5 5-5 5" fill="none" stroke="#fff" stroke-width="2"/></svg></span>
  </div>
  <ul class="member-list" style="left:835px;top:3058px">
    <li>• Graduates - Halvenor, school of massage therapy.</li>
    <li>• passion is Massage, stretching, and strength training to encourage postural restoration and realignment.</li>
    <li>• $75/ 60 minutes.</li>
    <li>• $95/ 90 minutes.</li>
    <li>• $120/ 120 minutes.</li>
  </ul>
</section>

<section class="contact abs" role="img" aria-label="Photo of a bright treatment room with a massage table"></section>
<div class="heading-rule" style="top:3392px"></div>
<h2 class="heading abs center" style="top:3405px">CONTACT US</h2>
<p class="script abs center on-dark" style="top:3460px">Send Us a Message</p>
<div class="field" style="left:82px;top:3536px;width:329px">Name</div>
<div class="field" style="left:432px;top:3536px;width:332px">E-Mail</div>
<div class="field" style="left:786px;top:3536px;width:332px">E-Mail</div>
<div class="field" style="left:82px;top:3601px;width:1036px;height:123px">Message</div>
<div class="submit abs">SUBMIT</div>

<section class="info abs"></section>
<div class="info-item" style="left:85px">
  <svg width="34" height="42" viewBox="0 0 24 30"><path d="M12 1a10 10 0 0 0-10 10c0 7 10 18 10 18s10-11 10-18A10 10 0 0 0 12 1z" fill="none" stroke="#fff" stroke-width="1.6"/><circle cx="12" cy="11" r="3.5" fill="none" stroke="#fff" stroke-width="1.6"/></svg>
  Marlow Bay, Washington 98000</div>
<div class="info-item" style="left:440px">
  <svg width="38" height="42" viewBox="0 0 24 24"><path d="M6.6 10.8a15 15 0 0 0 6.6 6.6l2.2-2.2c.3-.3.7-.4 1-.2 1.1.4 2.3.6 3.6.6.6 0 1 .4 1 1V20c0 .6-.4 1-1 1A17 17 0 0 1 3 4c0-.6.4-1 1-1h3.5c.6 0 1 .4 1 1 0 1.3.2 2.5.6 3.6.1.3 0 .7-.2 1z" fill="none" stroke="#fff" stroke-width="1.3"/></svg>
  (206) 555-0194</div>
<div class="info-item" style="left:792px">
  <svg width="40" height="42" viewBox="0 0 30 30"><rect x="3" y="6" width="24" height="18" fill="none" stroke="#fff" stroke-width="1.6"/><path d="M3 6l12 10 12-10" fill="none" stroke="#fff" stroke-width="1.6"/></svg>
  quarvenstretch@mailbrook.net</div>

<footer class="footer abs">
  <div class="copy">©2015 <b>QUARVEN TIDE</b>. All Rights Reserved</div>
  <div class="social" aria-label="Social links"><span></span><span></span><span></span><span></span></div>
</footer>

</body>
</html>
```